Gentleman's grooming products require a business card

I need a business card that incorporates the logo [ or parts of ] that we had Pixel Hive design for us as uploaded.

We sell online, mens grooming products including moustache waxes, beard oils and shaving accessories.
We want a card that is classy, professional and a card that shouts mens products.

Target Market(s)

Young professional male market

Industry/Entity Type

Business

Contact Information for Business Card

Ross and Edith Carwell
Lather and Lore
Purveyors of gentleman's stiffeners and grooming requisites
M :0418529647
E : ross@latherandlore.com.au
E : edith@latherandlore.com.au
E : sales@theblokesbalmery.com.au

W : www.latherandlore.com.au

Requirements
Must have
• Class
Nice to have
• Professionalism

```html
<!DOCTYPE html>
<html lang="en">
<head>
<meta charset="utf-8">
<title>Lather and Lore — Business Card</title>
<link rel="stylesheet" href="https://fonts.googleapis.com/css2?family=Cormorant+Garamond:wght@400;500&display=swap">
<style>
  :root {
    --page-bg: #d9d9d9;
    --card-black: #050505;
    --panel-black: #161616;
    --ink-white: #f2f2f2;
    --ink-grey: #bdbdbd;
    --rule: #e6e6e6;
  }
  * { box-sizing: border-box; margin: 0; padding: 0; }
  html, body {
    width: 1200px; height: 1000px; overflow: hidden;
    background: var(--page-bg);
  }
  .card {
    position: absolute; left: 75px; top: 200px;
    width: 1050px; height: 600px;
    background: var(--card-black);
    font-family: "Cormorant Garamond", Georgia, serif;
    color: var(--ink-white);
    box-shadow: 0 6px 18px rgba(0,0,0,0.25);
  }
  .card-frame {
    position: absolute; inset: 26px;
    border: 3px solid var(--rule);
    outline: 1px solid var(--rule);
    outline-offset: 5px;
  }
  .brand-panel {
    position: absolute; left: 150px; top: 56px;
    width: 760px; height: 270px;
    background: var(--panel-black);
  }
  .brand-rule-top {
    position: absolute; left: 40px; top: 64px; width: 520px; height: 2px;
    background: var(--rule);
  }
  .brand-name {
    position: absolute; left: 40px; top: 78px;
    font-size: 78px; font-weight: 500; line-height: 1;
    color: var(--ink-white);
    white-space: nowrap;
  }
  .brand-mark {
    position: absolute; left: 600px; top: 40px;
    width: 120px; height: 120px;
    border: 3px solid var(--rule);
  }
  .brand-rule-bottom {
    position: absolute; left: 40px; top: 182px; width: 680px; height: 2px;
    background: var(--rule);
  }
  .tagline {
    position: absolute; left: 40px; top: 196px;
    font-size: 17px; font-weight: 500; letter-spacing: 1.5px;
    font-variant: small-caps; text-transform: lowercase;
    color: var(--ink-grey); white-space: nowrap;
  }
  .contact {
    position: absolute; left: 190px; top: 350px;
    list-style: none;
  }
  .contact .phone {
    font-size: 36px; font-weight: 500; letter-spacing: 2px;
    margin-bottom: 10px;
  }
  .contact .email {
    font-size: 20px; color: var(--ink-grey); line-height: 1.35;
  }
  .contact .web {
    font-size: 34px; font-weight: 500; letter-spacing: 1px;
    margin-top: 12px;
  }
</style>
</head>
<body>
  <div class="card">
    <div class="card-frame"></div>
    <div class="brand-panel">
      <div class="brand-rule-top"></div>
      <div class="brand-name">Lather and Lore</div>
      <div class="brand-mark"></div>
      <div class="brand-rule-bottom"></div>
      <div class="tagline">Suppliers of Fine Tonics, Waxes and Shaving Essentials for Men</div>
    </div>
    <ul class="contact">
      <li class="phone">04 1852 9647</li>
      <li class="email">ross@latherandlore.com.au</li>
      <li class="email">edith@latherandlore.com.au</li>
      <li class="email">sales@theblokesbalmery.com.au</li>
      <li class="web">www.latherandlore.com.au</li>
    </ul>
  </div>
</body>
</html>
```